Tidewell Recovery Business Card Design

Professional and clean design. The design colors should flow with the logo. Two-sided card with the website on the back which is:

www.TidewellRecovery.example.

"Specializing in Water Damage Restoration"

On the front I need the name, email, phone, and logo.

Name: Dorian Vashti
Email: Dorian@TidewellRecovery.example
Phone: 555-318-2046 for now

I only have the Preview and Thumbnail right now but should have the source files uploaded within a day or two.

Target Market(s)

Flood victims, home owners with water damage from busted pipes etc...

Industry/Entity Type

Business

Contact Information for Business Card

Name: Dorian Vashti

Font styles to use
Serif
Sans Serif

```html
<!DOCTYPE html>
<html lang="en">
<head>
<meta charset="utf-8">
<title>Tidewell Recovery Business Card</title>
<link rel="stylesheet" href="https://fonts.googleapis.com/css2?family=Open+Sans:wght@400;600;700&display=swap">
<style>
  :root {
    --page-bg: #eef1f4;
    --card-white: #ffffff;
    --card-shade: #e9ecef;
    --brand-blue: #2f93d2;
    --brand-blue-deep: #1f7fc0;
    --brand-blue-light: #5bb6e8;
    --line-blue: #7cc8ef;
    --text-grey: #4a4a4a;
    --text-white: #ffffff;
  }
  * { margin: 0; padding: 0; box-sizing: border-box; }
  html, body { width: 1200px; height: 843px; overflow: hidden; }
  body {
    background: var(--page-bg);
    font-family: "Open Sans", Arial, sans-serif;
    display: flex;
    align-items: center;
    justify-content: center;
    gap: 44px;
  }
  .card {
    position: relative;
    width: 540px;
    height: 309px;
    border-radius: 22px;
    overflow: hidden;
    box-shadow: 0 8px 24px rgba(0,0,0,0.18);
  }
  /* Back side */
  .card-back {
    background: linear-gradient(160deg, var(--card-white) 55%, var(--card-shade));
    display: flex;
    flex-direction: column;
    align-items: center;
    justify-content: center;
  }
  .back-brand {
    display: flex;
    align-items: center;
    gap: 16px;
    margin-top: 10px;
  }
  .brand-dot {
    border-radius: 50%;
    background: var(--brand-blue);
    flex: none;
  }
  .back-brand .brand-dot { width: 62px; height: 62px; }
  .back-brand .brand-name {
    font-weight: 600;
    font-size: 30px;
    color: var(--brand-blue);
    letter-spacing: 0.5px;
  }
  .tagline {
    margin-top: 44px;
    font-size: 15px;
    font-weight: 600;
    color: var(--text-grey);
    letter-spacing: 0.3px;
  }
  /* Front side */
  .card-front { background: var(--card-white); }
  .front-wave {
    position: absolute;
    inset: 0;
    width: 100%;
    height: 100%;
  }
  .front-brand {
    position: absolute;
    top: 46px;
    left: 150px;
    display: flex;
    align-items: center;
    gap: 12px;
  }
  .front-brand .brand-dot { width: 38px; height: 38px; }
  .front-brand .brand-name {
    font-weight: 600;
    font-size: 25px;
    color: var(--brand-blue);
    letter-spacing: 0.5px;
  }
  .contact {
    position: absolute;
    left: 0;
    right: 0;
    top: 172px;
    text-align: center;
    color: var(--text-white);
  }
  .contact-name {
    font-weight: 700;
    font-size: 20px;
    margin-bottom: 6px;
    padding-left: 40px;
  }
  .contact-line {
    font-size: 14.5px;
    line-height: 1.45;
  }
</style>
</head>
<body>
  <section class="card card-back" aria-label="Business card back">
    <div class="back-brand">
      <span class="brand-dot"></span>
      <span class="brand-name">Tidewell Recovery</span>
    </div>
    <p class="tagline">Specializing in Water Damage Restoration</p>
  </section>

  <section class="card card-front" aria-label="Business card front">
    <svg class="front-wave" viewBox="0 0 540 309" preserveAspectRatio="none" aria-hidden="true">
      <defs>
        <linearGradient id="waveFill" x1="0" y1="0" x2="1" y2="1">
          <stop offset="0" stop-color="#5bb6e8"/>
          <stop offset="0.5" stop-color="#2f93d2"/>
          <stop offset="1" stop-color="#1f7fc0"/>
        </linearGradient>
      </defs>
      <path d="M0 30 C 90 140, 300 185, 540 168 L540 309 L0 309 Z" fill="url(#waveFill)"/>
      <path d="M0 14 C 90 124, 300 168, 540 152" fill="none" stroke="#7cc8ef" stroke-width="3"/>
    </svg>
    <div class="front-brand">
      <span class="brand-dot"></span>
      <span class="brand-name">Tidewell Recovery</span>
    </div>
    <div class="contact">
      <p class="contact-name">Dorian Vashti</p>
      <p class="contact-line">555-318-2046 | Dorian@TidewellRecovery.example</p>
      <p class="contact-line">www.TidewellRecovery.example</p>
    </div>
  </section>
</body>
</html>
```